Dr. Marissa Tevlin Medical/Chiropractic Business Card

Dr. Tevlin is a chiropractor and will require a business card that she uses every single day to book appointments on the back side of the card. Currently the office name goes by Dr. Marissa Tevlin. The chiropractic profession is based on the diagnosis and manipulative treatment of misalignments of the joints, especially those of the spinal column, which are held to cause other disorders by affecting the nerves, muscles, and organs. Dr. Marissa Tevlin is looking for a contemporary and minimalistic design.

Industry/Entity Type

Medical

Contact Information for Business Card

Name: Dr. Marissa Tevlin; Address: 748 Harcastle Rd South, London, ON N5R 2K7; Phone Number: 519.274.6193; Fax: 519.281.5046; email: marissa.tevlin@quorvamail.com

Requirements
Must have
• ability to write multiple appointments date/time on the back of card

```html
<!DOCTYPE html>
<html lang="en">
<head>
<meta charset="utf-8">
<title>Dr. Marissa Tevlin – Business Card</title>
<link rel="stylesheet" href="https://fonts.googleapis.com/css2?family=Montserrat:wght@600;700&family=Open+Sans:wght@400;600&display=swap">
<style>
  :root {
    --stage: #e4e4e4;
    --lime-light: #b4d65c;
    --lime: #9cc844;
    --lime-deep: #82b532;
    --charcoal: #1f2121;
    --ink: #1c1c1c;
    --paper: #ffffff;
    --paper-shade: #e6e6e6;
    --rule: #3a3a3a;
    --muscle: #b46a3e;
    --muscle-dark: #7a3f22;
  }
  * { box-sizing: border-box; margin: 0; padding: 0; }
  html, body { width: 1200px; height: 900px; overflow: hidden; }
  body {
    background: var(--stage);
    display: flex;
    flex-direction: column;
    align-items: center;
    justify-content: center;
    gap: 56px;
    font-family: "Open Sans", Arial, sans-serif;
  }
  .card {
    position: relative;
    width: 580px;
    height: 332px;
    overflow: hidden;
    box-shadow: 0 6px 18px rgba(0,0,0,0.18);
  }

  /* Front */
  .card-front {
    background: linear-gradient(100deg, var(--lime-light) 0%, var(--lime) 55%, var(--lime-deep) 100%);
  }
  .card-front .shapes { position: absolute; inset: 0; }
  .doctor-name {
    position: absolute;
    left: 44px;
    top: 44px;
    font-family: "Montserrat", Arial, sans-serif;
    font-weight: 700;
    font-size: 31px;
    letter-spacing: 0.2px;
    color: var(--ink);
    text-transform: uppercase;
  }
  .contact-list {
    position: absolute;
    left: 44px;
    top: 112px;
    list-style: none;
    color: var(--ink);
    font-size: 16px;
    line-height: 25px;
  }
  .contact-list li { display: flex; align-items: center; gap: 8px; }
  .contact-list svg { width: 15px; height: 15px; flex: none; }
  .address {
    position: absolute;
    left: 44px;
    top: 200px;
    font-size: 16px;
    line-height: 25px;
    color: var(--ink);
    font-style: normal;
  }

  /* Back */
  .card-back {
    background: linear-gradient(90deg, var(--paper) 0%, var(--paper) 35%, var(--paper-shade) 100%);
  }
  .card-back .shapes { position: absolute; inset: 0; }
  .appointments-title {
    position: absolute;
    left: 36px;
    top: 22px;
    font-family: "Montserrat", Arial, sans-serif;
    font-weight: 700;
    font-size: 26px;
    letter-spacing: 1.5px;
    color: var(--ink);
  }
  .column-label {
    position: absolute;
    top: 62px;
    font-size: 11px;
    letter-spacing: 0.5px;
    color: var(--ink);
  }
  .column-label.date { left: 38px; }
  .column-label.time { left: 310px; }
  .reschedule-note {
    position: absolute;
    left: 0;
    right: 0;
    bottom: 16px;
    text-align: center;
    font-size: 14px;
    line-height: 19px;
    color: var(--ink);
  }
</style>
</head>
<body>

  <section class="card card-front" aria-label="Business card front">
    <svg class="shapes" viewBox="0 0 580 332" width="580" height="332">
      <defs>
        <linearGradient id="anatomyTone" x1="0" y1="0" x2="1" y2="0">
          <stop offset="0" stop-color="var(--muscle)"/>
          <stop offset="0.5" stop-color="#c98552"/>
          <stop offset="1" stop-color="var(--muscle-dark)"/>
        </linearGradient>
      </defs>
      <path class="anatomy-area" role="img" aria-label="Illustration of a human back with muscles and spine, with silhouettes of people straightening from a hunched to an upright posture"
            d="M360 332 L375 40 Q390 0 430 0 L520 0 Q555 10 565 60 L580 300 L580 332 Z"
            fill="url(#anatomyTone)" opacity="0.9"/>
      <path class="base-band" d="M0 332 L0 292 Q300 284 580 218 L580 332 Z" fill="var(--charcoal)"/>
    </svg>
    <h1 class="doctor-name">Dr. Marissa Tevlin</h1>
    <ul class="contact-list">
      <li>
        <svg viewBox="0 0 16 16" aria-label="Phone"><path d="M3.5 1.5l2.5 0 1 3.5-1.6 1.2a9 9 0 0 0 4.4 4.4l1.2-1.6 3.5 1v2.5c0 .8-.7 1.5-1.5 1.5A12.5 12.5 0 0 1 2 3c0-.8.7-1.5 1.5-1.5z" fill="var(--ink)"/></svg>
        519.274.6193
      </li>
      <li>
        <svg viewBox="0 0 16 16" aria-label="Fax"><rect x="4" y="1" width="8" height="4" fill="var(--ink)"/><rect x="1" y="6" width="14" height="6" rx="1" fill="var(--ink)"/><rect x="4" y="10" width="8" height="5" fill="var(--ink)" stroke="var(--lime)" stroke-width="1"/></svg>
        519.281.5046
      </li>
      <li>
        <svg viewBox="0 0 16 16" aria-label="Email"><rect x="1" y="3" width="14" height="10" fill="var(--ink)"/><path d="M1.5 3.5 L8 9 L14.5 3.5" fill="none" stroke="var(--lime)" stroke-width="1.2"/></svg>
        marissa.tevlin@quorvamail.com
      </li>
    </ul>
    <address class="address">748 Harcastle Rd South,<br>London, ON N5R 2K7</address>
  </section>

  <section class="card card-back" aria-label="Business card back">
    <svg class="shapes" viewBox="0 0 580 332" width="580" height="332">
      <g class="write-lines" stroke="var(--rule)" stroke-width="1">
        <line x1="38" y1="100" x2="290" y2="100"/><line x1="310" y1="100" x2="545" y2="100"/>
        <line x1="38" y1="126" x2="290" y2="126"/><line x1="310" y1="126" x2="545" y2="126"/>
        <line x1="38" y1="152" x2="290" y2="152"/><line x1="310" y1="152" x2="545" y2="152"/>
        <line x1="38" y1="178" x2="290" y2="178"/><line x1="310" y1="178" x2="545" y2="178"/>
        <line x1="38" y1="204" x2="290" y2="204"/><line x1="310" y1="204" x2="545" y2="204"/>
        <line x1="38" y1="230" x2="290" y2="230"/><line x1="310" y1="230" x2="545" y2="230"/>
      </g>
      <path class="note-band" d="M0 332 L0 268 Q320 262 580 236 L580 332 Z" fill="var(--lime-deep)"/>
    </svg>
    <h2 class="appointments-title">APPOINTMENTS</h2>
    <span class="column-label date">DATE</span>
    <span class="column-label time">TIME</span>
    <p class="reschedule-note">If you are unable to make your appointment,<br>please call us to reschedule</p>
  </section>

</body>
</html>
```